M Zyvantics Buisness Cards

I need a technology focused clean business card for my employees. I have attached out logo to include in the mocks. We're a modern tech consulting firm that drives to interface humanity with technology in a truly cohesive fashion.

```html
<!DOCTYPE html>
<html lang="en">
<head>
<meta charset="utf-8">
<title>M Zyvantics Business Cards</title>
<link rel="stylesheet" href="https://fonts.googleapis.com/css2?family=Roboto:wght@400;500&family=Roboto+Condensed:wght@500;700&display=swap">
<style>
  :root {
    --brand-blue: #1b75bb;
    --ink-blue: #1e73b9;
    --ink-grey: #7a7a7a;
    --ink-dark: #555555;
    --card-white: #f2f2f2;
    --edge-grey: #77787b;
    --rule-grey: #b5b5b5;
    --backdrop: #b08a66;
  }
  * { margin: 0; padding: 0; box-sizing: border-box; }
  html, body { width: 1200px; height: 960px; overflow: hidden; }
  body {
    position: relative;
    background: var(--backdrop);
    font-family: "Roboto", Arial, sans-serif;
  }
  .card {
    position: absolute;
    width: 601px;
    height: 343px;
    box-shadow: 0 3px 6px rgba(0,0,0,0.35);
  }
  /* Front */
  .card-front {
    left: 314px; top: 113px;
    background: var(--card-white);
    border-left: 23px solid var(--brand-blue);
    border-right: 24px solid var(--edge-grey);
  }
  .identity {
    position: absolute;
    right: 314px; top: 145px;
    text-align: right;
    font-family: "Roboto Condensed", Arial, sans-serif;
  }
  .identity-name {
    color: var(--ink-blue);
    font-size: 22px;
    font-weight: 700;
    line-height: 1.1;
  }
  .identity-role {
    color: var(--ink-grey);
    font-size: 16px;
    font-weight: 500;
    margin-top: 4px;
  }
  .divider {
    position: absolute;
    left: 271px; top: 117px;
    width: 2px; height: 110px;
    background: var(--rule-grey);
  }
  .contact-list {
    position: absolute;
    left: 302px; top: 132px;
    list-style: none;
  }
  .contact-list li {
    display: flex;
    align-items: center;
    height: 19px;
    font-size: 14.5px;
    color: var(--ink-dark);
  }
  .contact-list svg {
    width: 14px; height: 14px;
    margin-right: 8px;
    fill: var(--ink-blue);
  }
  .address {
    position: absolute;
    left: 108px; top: 290px;
    display: flex;
    align-items: center;
    font-size: 14.5px;
    color: var(--ink-dark);
    white-space: pre;
  }
  .address svg { width: 14px; height: 16px; margin-right: 11px; fill: var(--ink-blue); }
  /* Back */
  .card-back {
    left: 311px; top: 472px;
    background: var(--brand-blue);
    color: #ffffff;
    text-align: center;
  }
  .brand-name {
    position: absolute;
    left: 0; right: 0; top: 136px;
    font-family: "Roboto", Arial, sans-serif;
    font-size: 56px;
    font-weight: 500;
    line-height: 1;
  }
  .web-address {
    position: absolute;
    left: 0; right: 0; top: 292px;
    font-size: 13px;
    letter-spacing: 6px;
  }
</style>
</head>
<body>
  <section class="card card-front">
    <div class="identity">
      <div class="identity-name">DANIEL MOREAU</div>
      <div class="identity-role">CEO/FOUNDER</div>
    </div>
    <div class="divider"></div>
    <ul class="contact-list">
      <li><svg viewBox="0 0 24 24"><path d="M6.6 10.8a15.1 15.1 0 0 0 6.6 6.6l2.2-2.2a1 1 0 0 1 1-.25 11.4 11.4 0 0 0 3.6.57 1 1 0 0 1 1 1V20a1 1 0 0 1-1 1A17 17 0 0 1 3 4a1 1 0 0 1 1-1h3.5a1 1 0 0 1 1 1c0 1.25.2 2.45.57 3.6a1 1 0 0 1-.25 1z"/></svg>555 214 7730</li>
      <li><svg viewBox="0 0 24 24"><path d="M7 1h10a2 2 0 0 1 2 2v18a2 2 0 0 1-2 2H7a2 2 0 0 1-2-2V3a2 2 0 0 1 2-2zm0 3v14h10V4zm5 15.5a1.2 1.2 0 1 0 0 2.4 1.2 1.2 0 0 0 0-2.4z"/></svg>555 382 6051</li>
      <li><svg viewBox="0 0 24 24"><path d="M6 2h12v6H6zM3 9h18a2 2 0 0 1 2 2v6h-4v5H5v-5H1v-6a2 2 0 0 1 2-2zm4 8v3h10v-3z"/></svg>555 907 4418</li>
      <li><svg viewBox="0 0 24 24"><path d="M2 5h20v14H2zm2 2v.5l8 5 8-5V7zm0 3v7h16v-7l-8 5z"/></svg>daniel@mzyvantics.com</li>
    </ul>
    <div class="address"><svg viewBox="0 0 24 28"><path d="M12 0a10 10 0 0 0-10 10c0 7.5 10 18 10 18s10-10.5 10-18A10 10 0 0 0 12 0zm0 14.5a4.5 4.5 0 1 1 0-9 4.5 4.5 0 0 1 0 9z"/></svg>4120 Larkspur Court  Fairbanks, Alaska 99701</div>
  </section>

  <section class="card card-back">
    <div class="brand-name">M Zyvantics</div>
    <div class="web-address">www.mzyvantics.com</div>
  </section>
</body>
</html>
```